" Consultoria técnica de gestão de empresas no setor alimentício. Administração, montagem de cardápios, dimensionamento e compra de equipamentos e gêneros, medição de resultados, controle de fluxo operacional, Controle de custos, contratação de prestadores de serviço, etc. "

```html
<!DOCTYPE html>
<html lang="pt-BR">
<head>
<meta charset="UTF-8">
<title>NOVARE Consultoria — Papelaria</title>
<link rel="stylesheet" href="https://fonts.googleapis.com/css2?family=Montserrat:wght@500&display=swap">
<style>
  :root {
    --bg: #e6e7e9;
    --paper: #ffffff;
    --navy: #0d2256;
    --flap: #6b6d72;
    --ink-light: #c9d0e2;
    --shadow: rgba(20, 24, 40, 0.18);
  }
  * { box-sizing: border-box; margin: 0; padding: 0; }
  html, body { width: 1200px; height: 1200px; overflow: hidden; }
  body {
    background: var(--bg);
    font-family: "Montserrat", sans-serif;
    position: relative;
  }
  .letterhead {
    position: absolute;
    left: 130px; top: 260px;
    width: 460px; height: 650px;
    background: var(--paper);
    border-bottom: 6px solid var(--navy);
    box-shadow: 0 10px 30px var(--shadow);
  }
  .letterhead .brand {
    position: absolute;
    top: 70px; left: 0; right: 0;
    text-align: center;
    color: var(--navy);
    font-size: 24px;
    font-weight: 500;
    letter-spacing: 2px;
    white-space: nowrap;
  }
  .envelope {
    position: absolute;
    left: 640px; top: 220px;
    width: 460px; height: 720px;
    background: var(--navy);
    box-shadow: 0 10px 30px var(--shadow);
    overflow: hidden;
  }
  .envelope .flap {
    position: absolute;
    top: 0; left: 0;
    width: 100%; height: 60px;
  }
  .envelope .flap-bottom {
    position: absolute;
    bottom: 0; left: 0;
    width: 100%; height: 14px;
    background: var(--flap);
  }
  .envelope .brand {
    position: absolute;
    bottom: 110px; left: 0; right: 0;
    text-align: center;
    color: var(--paper);
    font-size: 22px;
    font-weight: 500;
    letter-spacing: 2px;
    white-space: nowrap;
  }
  .contact-row {
    position: absolute;
    bottom: 50px; left: 24px; right: 24px;
    display: flex;
    justify-content: space-between;
    align-items: center;
    list-style: none;
  }
  .contact-row li {
    display: flex;
    align-items: center;
    gap: 5px;
    flex-shrink: 0;
    white-space: nowrap;
    color: var(--ink-light);
    font-size: 10px;
    font-weight: 500;
    line-height: 1;
  }
  .contact-row svg { width: 12px; height: 12px; fill: var(--paper); flex-shrink: 0; }
</style>
</head>
<body>
  <section class="letterhead">
    <div class="brand">NOVARE Consultoria</div>
  </section>

  <section class="envelope">
    <svg class="flap" viewBox="0 0 460 60" preserveAspectRatio="none" aria-hidden="true">
      <polygon points="0,0 460,0 460,40 440,60 20,60 0,40" fill="#6b6d72"/>
    </svg>
    <div class="brand">NOVARE Consultoria</div>
    <ul class="contact-row">
      <li>
        <svg viewBox="0 0 24 24" aria-hidden="true"><path d="M12 2a7 7 0 0 0-7 7c0 5 7 13 7 13s7-8 7-13a7 7 0 0 0-7-7zm0 9.5A2.5 2.5 0 1 1 12 6.5a2.5 2.5 0 0 1 0 5z"/></svg>
        Rua das Palmeiras, 120 Centro
      </li>
      <li>
        <svg viewBox="0 0 24 24" aria-hidden="true"><path d="M2 5h20v14H2zm2 2v.5l8 5 8-5V7z"/></svg>
        contato@novare.com
      </li>
      <li>
        <svg viewBox="0 0 24 24" aria-hidden="true"><path d="M6.6 10.8a15 15 0 0 0 6.6 6.6l2.2-2.2a1 1 0 0 1 1-.25 11.4 11.4 0 0 0 3.6.57 1 1 0 0 1 1 1V20a1 1 0 0 1-1 1A17 17 0 0 1 3 4a1 1 0 0 1 1-1h3.5a1 1 0 0 1 1 1c0 1.25.2 2.45.57 3.6a1 1 0 0 1-.25 1z"/></svg>
        (11) 5555-0134
      </li>
    </ul>
    <div class="flap-bottom"></div>
  </section>
</body>
</html>
```